Grow Stronger With Marla Sunrise Group Workout

We need to launch a grand opening for March of 2016. We offer early morning 6 am to 7 am group exercise.
Two Programs: Mon/Wed/Fri - 3X/week OR Tues/Thurs - 2X/week.
All programs have optional Steadfast Fuel Coaching. Space is limited to 20 persons for each program.
Please use purple and red as two of the colours.
My business name is Grow Stronger With Marla Ltd
I don't know what else I need to supply to create the flyer...I have no experience with this sort of thing. Whatever the .designers come up with that is appropriate for a group fitness workout that will convey people having fun, energetic and uplifting.
This will be an indoor and outdoor group fitness workout.
Pre-registration is required. Come and try a complimentary session.
Contact information:
Trainer: Marla Trevin
Business name: Grow Stronger With Marla Ltd
Certifications: Personal Trainer
Steadfast Fuel Coach level 1
Nutrition & Wellness Specialist
Korvel Bootcamp
Business number: 604-519-3806
email: growstrongerwithmarla@fitmailbox.test
General public, male and female over age of consent
Group
Grow Stronger With Marla
- I'd like to see some pictures, photographs of people of different shapes and sizes generally having fun while doing a group outdoor/indoor workout.

```html
<!DOCTYPE html>
<html lang="en">
<head>
<meta charset="utf-8">
<title>Grow Stronger With Marla – Grand Opening</title>
<link href="https://fonts.googleapis.com/css2?family=Roboto+Condensed:wght@400;700&family=Russo+One&family=Open+Sans:wght@400;700&family=Arimo&display=swap" rel="stylesheet">
<style>
  :root{
    --red:#e3202a;
    --purple:#5b2d91;
    --purple-light:#7c4fb4;
    --purple-dark:#4a2180;
    --ink:#1c1c1c;
    --band:#161616;
    --footer:#242424;
    --white:#ffffff;
    --soft:#e6e6e6;
    --photo-a:#6fa53a;
    --photo-b:#c9d98a;
  }
  *{margin:0;padding:0;box-sizing:border-box}
  html,body{width:907px;height:1200px;overflow:hidden;background:#fff}
  .flyer{position:relative;width:907px;height:1200px;overflow:hidden;background:var(--white);font-family:"Roboto Condensed",sans-serif}
  .artwork{position:absolute;inset:0}
  .abs{position:absolute;white-space:nowrap}

  .t-cond{font-family:"Roboto Condensed",sans-serif}
  .t-bold{font-weight:700}
  .t-reg{font-weight:400}
  .t-year{font-family:"Russo One",sans-serif}
  .fill-red{fill:var(--red)}
  .fill-ink{fill:var(--ink)}
  .fill-white{fill:var(--white)}

  .intro{left:32px;top:612px;width:431px;height:158px;overflow:hidden;white-space:normal;font-family:"Open Sans",sans-serif;font-size:13.2px;line-height:17.5px;color:var(--ink);text-align:justify}

  .trainer{left:32px;top:815px;font-size:38px;font-weight:700;color:var(--ink);line-height:1}
  .trainer span{color:var(--red)}
  .role{left:32px;top:857px;font-size:38px;font-weight:700;color:var(--ink);line-height:1}
  .business{left:32px;top:904px;font-family:"Open Sans",sans-serif;font-size:20px;font-weight:700;color:var(--purple);line-height:1}
  .specialist{left:32px;top:952px;width:386px;height:42px;border-radius:14px;background:var(--red);color:var(--white);font-family:"Open Sans",sans-serif;font-size:20px;font-weight:700;line-height:42px;text-align:center}

  .phone{left:75px;top:1040px;font-size:34px;font-weight:700;color:var(--white);line-height:1}
  .creds{left:77px;top:1081px;font-family:"Arimo",sans-serif;font-size:14px;line-height:19px;color:var(--soft)}
  .email{left:77px;top:1119px;font-family:"Arimo",sans-serif;font-size:14px;line-height:19px;color:var(--soft)}
</style>
</head>
<body>
<main class="flyer">
  <svg class="artwork" width="907" height="1200" viewBox="0 0 907 1200">
    <defs>
      <linearGradient id="photoTone" x1="0" y1="0" x2="1" y2="1">
        <stop offset="0" stop-color="#5e9a30"/>
        <stop offset="1" stop-color="var(--photo-b)"/>
      </linearGradient>
      <linearGradient id="ribbonTone" x1="0" y1="0" x2="0" y2="1">
        <stop offset="0" stop-color="var(--purple-light)"/>
        <stop offset="1" stop-color="var(--purple-dark)"/>
      </linearGradient>
      <linearGradient id="bandTone" x1="0" y1="0" x2="0" y2="1">
        <stop offset="0" stop-color="#2a2a2a"/>
        <stop offset="1" stop-color="var(--band)"/>
      </linearGradient>
      <radialGradient id="portraitTone" cx="0.5" cy="0.45" r="0.6">
        <stop offset="0" stop-color="#c9a58a"/>
        <stop offset="1" stop-color="#4b3a33"/>
      </radialGradient>
    </defs>

    <!-- hero photo -->
    <path role="img" aria-label="Photo of two smiling children in a sunny garden carrying fresh carrots and a small wheelbarrow of vegetables"
          d="M0,0 H470 C498,120 512,300 505,434 H0 Z" fill="url(#photoTone)"/>
    <path d="M470,0 C498,120 512,300 505,434" fill="none" stroke="var(--purple)" stroke-width="9"/>

    <!-- headline -->
    <text class="t-cond t-bold fill-red" x="545" y="118" font-size="124" textLength="328" lengthAdjust="spacingAndGlyphs">GRAND</text>
    <text class="t-cond t-bold fill-red" x="545" y="220" font-size="118" textLength="328" lengthAdjust="spacingAndGlyphs">OPENING</text>
    <text class="t-cond t-bold fill-ink" x="545" y="276" font-size="60" textLength="328" lengthAdjust="spacingAndGlyphs">for March of</text>
    <rect x="512" y="296" width="395" height="7" fill="var(--purple)"/>
    <text class="t-year fill-ink" x="545" y="389" font-size="86" textLength="328" lengthAdjust="spacingAndGlyphs">2016</text>
    <rect x="505" y="420" width="402" height="7" fill="var(--purple)"/>

    <!-- info band -->
    <rect x="0" y="434" width="907" height="139" fill="url(#bandTone)"/>
    <text class="t-cond t-bold fill-white" x="28" y="496" font-size="32" textLength="349" lengthAdjust="spacingAndGlyphs">We offer early morning</text>
    <text class="t-cond t-reg fill-white" x="28" y="533" font-size="30" textLength="352" lengthAdjust="spacingAndGlyphs"><tspan class="t-bold fill-red">6</tspan><tspan class="fill-red"> am</tspan> to <tspan class="t-bold fill-red">7</tspan><tspan class="fill-red"> am</tspan> group exercise</text>
    <text class="t-cond t-bold fill-white" x="497" y="496" font-size="36" textLength="355" lengthAdjust="spacingAndGlyphs">Mon/Wed/Fri - 3X/week</text>
    <text class="t-cond t-bold fill-white" x="497" y="538" font-size="36" textLength="325" lengthAdjust="spacingAndGlyphs">Tues/Thurs - 2X/week</text>

    <!-- purple ribbon -->
    <path d="M503,573 H866 V846 C810,825 750,815 685,815 C620,815 560,825 503,846 Z" fill="url(#ribbonTone)"/>
    <text class="t-cond t-bold fill-white" x="546" y="642" font-size="40" textLength="277" lengthAdjust="spacingAndGlyphs">Pre-registration</text>
    <text class="t-cond t-reg fill-white" x="546" y="704" font-size="58" textLength="277" lengthAdjust="spacingAndGlyphs">is required</text>
    <text class="t-cond t-bold fill-white" x="546" y="780" font-size="44" textLength="277" lengthAdjust="spacingAndGlyphs">Come and try</text>
    <text class="t-cond t-reg fill-white" x="544" y="811" font-size="26" textLength="279" lengthAdjust="spacingAndGlyphs">a complimentary session</text>

    <!-- footer -->
    <path d="M0,1014 H380 C440,1014 460,1099 540,1099 H907" fill="none" stroke="var(--purple)" stroke-width="4"/>
    <path d="M0,1020 H380 C440,1020 460,1105 540,1105 H907 V1200 H0 Z" fill="var(--footer)"/>

    <!-- portrait -->
    <circle cx="695" cy="969" r="124" fill="var(--white)"/>
    <circle cx="695" cy="969" r="119" fill="none" stroke="var(--purple)" stroke-width="6"/>
    <circle role="img" aria-label="Portrait photo of trainer Marla Trevin" cx="695" cy="969" r="110" fill="url(#portraitTone)"/>

    <!-- phone icon -->
    <circle cx="55" cy="1059" r="8" fill="none" stroke="#9b7cc8" stroke-width="2"/>
    <path d="M51,1055 l3,0 l1,3 l-2,1 a6,6 0 0 0 3,3 l1,-2 l3,1 l0,3 a9,9 0 0 1 -9,-9 z" fill="#9b7cc8"/>
    <!-- mail icon -->
    <rect x="47" y="1122" width="18" height="12" rx="1" fill="var(--purple-light)"/>
    <path d="M47,1123 l9,7 l9,-7" fill="none" stroke="var(--footer)" stroke-width="1.5"/>
  </svg>

  <p class="abs intro">We only have one life to live; our body is our temple. Invest in your temple...invest in yourself. Grow Stronger With Marla to create sustainable healthy lifestyle through daily quality nutrition and active living<br>Grow Stronger With Marla will work with you to find the nutrition, exercise and stress-management strategies that fit easily in to your life. Helping you to take control of your life and fitness again without unsustainable fads, quick-fixes and confusing advise. Instead we will provide coaching programs suing the most-up-to-date health, fitness, nutrition and</p>

  <p class="abs trainer">Trainer- <span>Marla Trevin</span></p>
  <p class="abs role">Personal Trainer</p>
  <p class="abs business">Grow Stronger With Marla Ltd</p>
  <p class="abs specialist">Nutrition &amp; Wellness Specialist</p>

  <p class="abs phone">604-519-3806</p>
  <p class="abs creds">Steadfast Fuel Coach level 1<br>Korvel Bootcamp</p>
  <p class="abs email">www.growstrongerwithmarla@fitmailbox.test</p>
</main>
</body>
</html>
```